Lom Consulting -New consulting business in architecture, urban planning, and real estate development

We need a stationery design, including logo, business cards, etc, work for a new consulting business that works in the world of architectural, urban planning and real estate development.

The name of the company is "Lom Consulting". Lom is my last name but it of course also has the meaning 'cool' and 'hip'.

Target Market(s)

The business will provide boutique consulting services to high end clients that may include property developers, cities, etc.

Industry/Entity Type

Consultant

Contact Information for Business Card

LOM Consulting
First Name Last Name
Title
Phone number
Address
Website
Optional: Twitter handle

Logo Text

LOM Consulting

Font styles to use
Sans Serif

Colors

Designer to choose colors to be used in the design.

Requirements
Must have
• Simple design
• Easy to read font
• Modern
• Elegance
• Nice font that can be used for future reports, letters, etc.
• Good colour scheme that allows for the elegance to come through
Should not have
• Complex design ideas
• Complex logos
• Not a corporate feel and look

```html
<!DOCTYPE html>
<html lang="en">
<head>
<meta charset="utf-8">
<title>Lom Consulting – Stationery Elements</title>
<link rel="stylesheet" href="https://fonts.googleapis.com/css2?family=Barlow+Semi+Condensed:wght@300;400;600&display=swap">
<style>
  :root {
    --brand-red: #be1e2d;
    --charcoal: #454547;
    --paper: #ffffff;
    --mist: #e6e6e7;
    --ink: #58585a;
    --title-ink: #3c3c3e;
    --page: #ffffff;
  }
  html, body {
    margin: 0;
    width: 1200px;
    height: 1200px;
    overflow: hidden;
    background: var(--page);
  }
  .board { display: block; width: 1200px; height: 1200px; }
  .board text { font-family: "Barlow Semi Condensed", Arial, sans-serif; }
  .board-title { font-size: 45px; fill: var(--title-ink); letter-spacing: 1.5px; }
  .board-title .strong { font-weight: 600; }
  .board-title .light { font-weight: 300; }

  .fill-red { fill: var(--brand-red); }
  .fill-charcoal { fill: var(--charcoal); }
  .fill-paper { fill: var(--paper); }
  .fill-mist { fill: var(--mist); }
  .sheet { filter: url(#lift); }

  .wordmark { font-weight: 400; text-anchor: middle; }
  .wordmark--red { fill: var(--brand-red); }
  .wordmark--white { fill: var(--paper); }
  .wordmark--ink { fill: var(--ink); }

  .contact { font-size: 5.6px; font-weight: 400; fill: var(--ink); }
  .contact--white { fill: var(--paper); font-weight: 600; font-size: 5px; }
  .icon--ink { fill: var(--ink); }
  .icon--white { fill: var(--paper); }

  .card-name { font-size: 5.4px; fill: var(--paper); letter-spacing: 0.8px; }
  .card-detail { font-size: 4.6px; fill: var(--paper); }
  .spiral-ring { fill: var(--paper); stroke: #bfbfc1; stroke-width: 0.6; }
  .bag-handle { fill: none; stroke: var(--paper); stroke-width: 4; }
  .bag-handle-edge { fill: none; stroke: #d0d0d2; stroke-width: 5.5; }
</style>
</head>
<body>
<svg class="board" viewBox="0 0 1000 1000" xmlns="http://www.w3.org/2000/svg" aria-label="Lom Consulting stationery elements">
  <defs>
    <filter id="lift" x="-10%" y="-10%" width="125%" height="125%">
      <feDropShadow dx="3" dy="4" stdDeviation="3" flood-color="#000" flood-opacity="0.28"/>
    </filter>
    <symbol id="icon-phone" viewBox="0 0 10 10">
      <path d="M2 1 L4 1 L4.6 3.4 L3.4 4.2 Q4.4 6 5.8 6.6 L6.6 5.4 L9 6 L9 8 Q9 9 8 9 Q1 8.4 1 2 Q1 1 2 1 Z"/>
    </symbol>
    <symbol id="icon-mail" viewBox="0 0 10 10">
      <path d="M1 2.5 H9 V7.5 H1 Z M1.6 3 L5 5.6 L8.4 3 Z" fill-rule="evenodd"/>
    </symbol>
    <symbol id="icon-pin" viewBox="0 0 10 10">
      <path d="M5 0.8 A3.2 3.2 0 0 1 8.2 4 C8.2 6.2 5 9.4 5 9.4 C5 9.4 1.8 6.2 1.8 4 A3.2 3.2 0 0 1 5 0.8 Z M5 2.7 A1.3 1.3 0 1 0 5 5.3 A1.3 1.3 0 1 0 5 2.7 Z" fill-rule="evenodd"/>
    </symbol>
  </defs>

  <!-- Board title -->
  <text class="board-title" x="500" y="66" text-anchor="middle"><tspan class="strong">LOM COSULTING</tspan><tspan class="light"> STATIONERY ELEMENTS</tspan></text>

  <!-- Letterhead -->
  <g class="letterhead">
    <rect class="sheet fill-paper" x="66" y="110" width="260" height="368"/>
    <polygon class="fill-charcoal" points="286,128 326,128 326,162"/>
    <polygon class="fill-red" points="286,128 306,128 306,145"/>
    <circle class="fill-red" cx="92" cy="145" r="4"/>
    <text class="wordmark wordmark--red" x="102" y="168" font-size="7">Lom Consulting</text>
    <use href="#icon-phone" class="icon--ink" x="139" y="139" width="5" height="5"/>
    <text class="contact" x="148" y="143.5">(000) 123456789</text>
    <use href="#icon-mail" class="icon--ink" x="139" y="149.5" width="5" height="5"/>
    <text class="contact" x="148" y="154">info@companyname.com</text>
    <use href="#icon-pin" class="icon--ink" x="139" y="160" width="5" height="5"/>
    <text class="contact" x="148" y="164.5">Street address 123</text>
  </g>

  <!-- Presentation folder -->
  <g class="folder">
    <rect class="sheet fill-paper" x="682" y="108" width="262" height="367"/>
    <polygon class="sheet fill-red" points="372,138 392,108 682,108 682,475 423,475 372,440"/>
    <polygon class="fill-charcoal" points="423,365 470,414 423,475"/>
    <polygon class="fill-charcoal" points="423,475 682,475 645,537 423,537"/>
    <circle class="fill-red" cx="812" cy="262" r="10"/>
    <text class="wordmark wordmark--ink" x="812" y="323" font-size="17">Lom Consulting</text>
    <text class="wordmark wordmark--white" x="550" y="421" font-size="7">Lom Consulting</text>
    <use href="#icon-phone" class="icon--white" x="452" y="443" width="6" height="6"/>
    <text class="contact contact--white" x="462" y="448">(000) 123456789</text>
    <use href="#icon-mail" class="icon--white" x="516" y="443" width="6" height="6"/>
    <text class="contact contact--white" x="526" y="448">info@companyname.com</text>
    <use href="#icon-pin" class="icon--white" x="598" y="443" width="6" height="6"/>
    <text class="contact contact--white" x="608" y="448">Street address 123</text>
  </g>

  <!-- Envelope -->
  <g class="envelope">
    <rect class="sheet fill-paper" x="66" y="548" width="264" height="142"/>
    <polygon class="fill-charcoal" points="66,548 330,548 330,565 66,565"/>
    <polygon class="fill-red" points="287,603 330,582 330,616"/>
    <rect class="fill-mist" x="202" y="621" width="99" height="40"/>
    <circle class="fill-red" cx="103" cy="598" r="4"/>
    <text class="wordmark wordmark--red" x="104" y="620" font-size="7">Lom Consulting</text>
    <use href="#icon-phone" class="icon--ink" x="83" y="632" width="5" height="5"/>
    <text class="contact" x="92" y="636.5">(000) 123456789</text>
    <use href="#icon-mail" class="icon--ink" x="83" y="643" width="5" height="5"/>
    <text class="contact" x="92" y="647.5">info@companyname.com</text>
    <use href="#icon-pin" class="icon--ink" x="83" y="654" width="5" height="5"/>
    <text class="contact" x="92" y="658.5">Street address 123</text>
  </g>

  <!-- Shopping bag -->
  <g class="shopping-bag">
    <path class="bag-handle-edge" d="M442 625 C442 560 556 560 556 625"/>
    <path class="bag-handle" d="M442 625 C442 560 556 560 556 625"/>
    <rect class="sheet fill-red" x="390" y="612" width="220" height="306"/>
    <polygon class="fill-charcoal" points="610,820 610,918 553,918"/>
    <circle fill="#000" cx="442" cy="625" r="5"/>
    <circle fill="#000" cx="556" cy="625" r="5"/>
    <path class="bag-handle" d="M442 625 C442 580 556 580 556 625" opacity="0"/>
    <circle class="fill-paper" cx="502" cy="700" r="8"/>
    <text class="wordmark wordmark--white" x="502" y="753" font-size="17">Lom Consulting</text>
  </g>

  <!-- Business cards -->
  <g class="business-card business-card--front">
    <rect class="sheet fill-charcoal" x="680" y="531" width="150" height="84" role="img" aria-label="Charcoal low-poly texture"/>
    <polygon class="fill-mist" points="813,531 830,531 830,568"/>
    <polygon class="fill-red" points="774,615 830,568 830,615"/>
    <circle class="fill-red" cx="735" cy="566" r="5"/>
    <text class="wordmark wordmark--white" x="735" y="592" font-size="8">Lom Consulting</text>
  </g>
  <g class="business-card business-card--back">
    <rect class="sheet fill-charcoal" x="778" y="589" width="152" height="84" role="img" aria-label="Charcoal low-poly texture"/>
    <polygon class="fill-mist" points="904,589 930,589 930,673 916,673"/>
    <polygon class="fill-red" points="897,589 930,589 930,612"/>
    <text class="card-name" x="833" y="615">FULL NAME HERE</text>
    <rect class="fill-red" x="833" y="619" width="56" height="0.8"/>
    <text class="card-detail" x="838" y="637">Street address 123</text>
    <text class="card-detail" x="838" y="646">(000) 123456789</text>
    <text class="card-detail" x="830" y="655">info@companyname.com</text>
  </g>

  <!-- CD and case -->
  <g class="cd">
    <circle class="sheet fill-charcoal" cx="270" cy="838" r="78" role="img" aria-label="Charcoal low-poly texture"/>
    <circle class="fill-mist" cx="270" cy="838" r="33"/>
    <circle fill="#c9c9cb" cx="270" cy="838" r="13"/>
    <polygon class="fill-red" points="298,840 340,818 336,856"/>
    <circle class="fill-red" cx="270" cy="785" r="5"/>
    <text class="wordmark wordmark--white" x="268" y="893" font-size="13">Lom Consulting</text>
  </g>
  <g class="cd-case">
    <rect class="sheet fill-charcoal" x="63" y="752" width="172" height="170" role="img" aria-label="Charcoal low-poly texture"/>
    <polygon class="fill-red" points="63,752 120,752 63,805"/>
    <polygon class="fill-mist" points="63,805 70,805 104,922 63,922"/>
    <circle class="fill-red" cx="155" cy="818" r="7"/>
    <text class="wordmark wordmark--white" x="155" y="872" font-size="14">Lom Consulting</text>
  </g>

  <!-- Spiral notebook -->
  <g class="notebook">
    <rect class="sheet fill-charcoal" x="672" y="716" width="250" height="202" role="img" aria-label="Charcoal low-poly texture"/>
    <polygon class="fill-mist" points="870,716 922,716 922,858 905,858"/>
    <polygon class="fill-red" points="864,918 922,858 922,918"/>
    <g class="spiral">
      <rect class="spiral-ring" x="664" y="724" width="16" height="5" rx="2.5"/>
      <rect class="spiral-ring" x="664" y="735" width="16" height="5" rx="2.5"/>
      <rect class="spiral-ring" x="664" y="746" width="16" height="5" rx="2.5"/>
      <rect class="spiral-ring" x="664" y="757" width="16" height="5" rx="2.5"/>
      <rect class="spiral-ring" x="664" y="768" width="16" height="5" rx="2.5"/>
      <rect class="spiral-ring" x="664" y="779" width="16" height="5" rx="2.5"/>
      <rect class="spiral-ring" x="664" y="790" width="16" height="5" rx="2.5"/>
      <rect class="spiral-ring" x="664" y="801" width="16" height="5" rx="2.5"/>
      <rect class="spiral-ring" x="664" y="812" width="16" height="5" rx="2.5"/>
      <rect class="spiral-ring" x="664" y="823" width="16" height="5" rx="2.5"/>
      <rect class="spiral-ring" x="664" y="834" width="16" height="5" rx="2.5"/>
      <rect class="spiral-ring" x="664" y="845" width="16" height="5" rx="2.5"/>
      <rect class="spiral-ring" x="664" y="856" width="16" height="5" rx="2.5"/>
      <rect class="spiral-ring" x="664" y="867" width="16" height="5" rx="2.5"/>
      <rect class="spiral-ring" x="664" y="878" width="16" height="5" rx="2.5"/>
      <rect class="spiral-ring" x="664" y="889" width="16" height="5" rx="2.5"/>
      <rect class="spiral-ring" x="664" y="900" width="16" height="5" rx="2.5"/>
    </g>
    <circle class="fill-red" cx="792" cy="792" r="7"/>
    <text class="wordmark wordmark--white" x="792" y="834" font-size="12">Lom Consulting</text>
  </g>
</svg>
</body>
</html>
```